Harbinger Crude Advisors needs a logo design and business card layout.

HCA is a consulting firm in oil and gas, specializing in upstream engineering and field work. We provide engineering solutions for the complete wellbore cycle from casing design to flowback. This includes completion and production design. On-site job supervision and project engineering for conventional and unconventional reservoirs. Asset analysis by reviewing operational conditions of asset packages to determine value of potential acquisitions or divesture.

```html
<!DOCTYPE html>
<html lang="en">
<head>
<meta charset="utf-8">
<title>Harbinger Crude Advisors — Business Card</title>
<link href="https://fonts.googleapis.com/css2?family=Arimo:wght@400;700&display=swap" rel="stylesheet">
<style>
  :root {
    --backdrop: #2a2a2b;
    --card: #1e2124;
    --grey: #9b9b9b;
    --text-grey: #8e8e8e;
    --yellow: #f2c10f;
  }
  * { box-sizing: border-box; margin: 0; padding: 0; }
  html, body {
    width: 1200px; height: 1189px; overflow: hidden;
    background: var(--backdrop);
    font-family: "Arimo", Arial, sans-serif;
  }
  .canvas {
    position: relative; width: 1200px; height: 1189px;
    display: flex; flex-direction: column; align-items: center; justify-content: center;
    gap: 70px;
  }
  .card {
    position: relative; width: 760px; height: 434px;
    background: var(--card); border-radius: 26px;
    box-shadow: 0 18px 40px rgba(0,0,0,.45);
  }
  .brand {
    display: flex; align-items: center; gap: 16px;
  }
  .brand-dot {
    width: 30px; height: 30px; border-radius: 50%; background: var(--yellow); flex: none;
  }
  .brand-name {
    font-weight: 700; color: var(--grey); line-height: 1.05;
  }
  .card-front { display: flex; align-items: center; justify-content: center; }
  .card-front .brand-name { font-size: 44px; }

  .card-back .brand {
    position: absolute; left: 56px; top: 50%; transform: translateY(-50%);
  }
  .card-back .brand-name { font-size: 30px; width: 250px; }
  .divider {
    position: absolute; left: 382px; top: 96px; width: 2px; height: 190px;
    background: var(--yellow);
  }
  .contact {
    position: absolute; left: 418px; top: 96px;
  }
  .person-name { font-weight: 700; font-size: 24px; color: var(--text-grey); }
  .person-role { font-size: 18px; color: var(--yellow); margin-top: 2px; }
  .contact-list { list-style: none; margin-top: 24px; display: grid; gap: 10px; }
  .contact-list li {
    display: flex; align-items: center; gap: 12px;
    font-size: 19px; color: var(--text-grey);
  }
  .contact-list .accent { color: var(--yellow); }
  .icon {
    width: 24px; height: 24px; border-radius: 50%; background: var(--yellow);
    display: flex; align-items: center; justify-content: center; flex: none;
  }
  .icon svg { width: 14px; height: 14px; }
</style>
</head>
<body>
<main class="canvas">
  <section class="card card-front" aria-label="Card front">
    <div class="brand">
      <span class="brand-dot"></span>
      <span class="brand-name">Harbinger Crude Advisors</span>
    </div>
  </section>

  <section class="card card-back" aria-label="Card back">
    <div class="brand">
      <span class="brand-dot"></span>
      <span class="brand-name">Harbinger Crude Advisors</span>
    </div>
    <span class="divider"></span>
    <div class="contact">
      <p class="person-name">Dana Whitlock</p>
      <p class="person-role">Director</p>
      <ul class="contact-list">
        <li>
          <span class="icon"><svg viewBox="0 0 16 16"><path d="M4 2l2 3-1.5 1.5a8 8 0 0 0 5 5L11 10l3 2-1 2.5C7 14 2 9 1.5 3z" fill="#1e2124"/></svg></span>
          555-014-2270
        </li>
        <li>
          <span class="icon"><svg viewBox="0 0 16 16"><rect x="4" y="1.5" width="8" height="13" rx="1.5" fill="none" stroke="#1e2124" stroke-width="1.8"/><circle cx="8" cy="12" r="1" fill="#1e2124"/></svg></span>
          555-014-3381
        </li>
        <li>
          <span class="icon"><svg viewBox="0 0 16 16"><rect x="1.5" y="3.5" width="13" height="9" fill="none" stroke="#1e2124" stroke-width="1.6"/><path d="M1.5 3.5l6.5 5 6.5-5" fill="none" stroke="#1e2124" stroke-width="1.6"/></svg></span>
          info@harbingercrude.com
        </li>
        <li>
          <span class="icon"><svg viewBox="0 0 16 16"><circle cx="8" cy="8" r="6" fill="none" stroke="#1e2124" stroke-width="1.5"/><ellipse cx="8" cy="8" rx="2.6" ry="6" fill="none" stroke="#1e2124" stroke-width="1.2"/><path d="M2 8h12" stroke="#1e2124" stroke-width="1.2"/></svg></span>
          <span>www.<span class="accent">harbingercrude</span>.com</span>
        </li>
      </ul>
    </div>
  </section>
</main>
</body>
</html>
```